Southport Billboard for Hiring more CDL drivers

I need a catch design for a bill board (size 10ft by 36 ft) to catch the attention for semi truck drivers.
In the design I want it to include:
-My company logo along with my website(brisklanefreighters.com) and my number(503-217-6095) for contact info.
-I also need it to say earn up to $90,000 a year
-I will send a few photos to choose from
-I need the logo to look clean and simple! I don't want it to be cluttered just clean, simple and catchy.!

Target Market(s)

CDL Class A holders
Semi Truck Drivers

Industry/Entity Type

Trucking Company

Font styles to use
Other font styles liked:
• a font to match my logo

Requirements
Must have
• "Make up to $90,000"
"brisklanefreighters.com"
"503-217-6095"

```html
<!DOCTYPE html>
<html lang="en">
<head>
<meta charset="utf-8">
<title>Brisk Lane Freighters – Driver Hiring Billboard</title>
<link rel="stylesheet" href="https://fonts.googleapis.com/css2?family=Oswald:wght@600&family=Open+Sans:wght@800&display=swap">
<style>
  :root {
    --page-bg: #ffffff;
    --board-blue: #10298c;
    --board-blue-deep: #0b1f6e;
    --accent-yellow: #f7c812;
    --accent-sky: #1a9be8;
    --ink-black: #111111;
    --text-white: #ffffff;
    --band-dark: #0a0f2e;
    --truck-tone-light: #b9c6bb;
    --truck-tone-dark: #6f7d73;
  }
  * { margin: 0; padding: 0; box-sizing: border-box; }
  html, body {
    width: 1200px; height: 1000px; overflow: hidden;
    background: var(--page-bg);
  }
  .billboard {
    position: absolute;
    left: 102px; top: 362px;
    width: 998px; height: 275px;
    background: var(--board-blue);
    overflow: hidden;
    box-shadow: 0 6px 14px rgba(0,0,0,0.25);
  }
  .headline {
    position: absolute; left: 22px; top: 10px;
    font-family: "Oswald", sans-serif; font-weight: 600;
    font-size: 62px; line-height: 1;
    color: var(--text-white);
    white-space: nowrap;
  }
  .headline-intro { display: inline-block; vertical-align: middle; margin-right: 18px; }
  .pay-badge {
    display: inline-block; vertical-align: middle;
    background: var(--accent-yellow);
    color: var(--ink-black);
    border-radius: 12px;
    padding: 6px 14px 8px;
    font-size: 62px;
  }
  .company-name {
    position: absolute; left: 22px; top: 122px;
    font-family: "Oswald", sans-serif; font-weight: 600;
    font-size: 34px; line-height: 1; letter-spacing: 1px;
    color: var(--text-white);
    text-transform: uppercase;
  }
  .website {
    position: absolute; left: 22px; top: 194px;
    font-family: "Open Sans", sans-serif; font-weight: 800;
    font-size: 17px; color: var(--text-white);
  }
  .phone-band {
    position: absolute; left: 0; top: 226px;
    width: 620px; height: 49px;
    background: linear-gradient(90deg, var(--band-dark) 0%, var(--band-dark) 45%, rgba(10,15,46,0) 100%);
  }
  .phone {
    position: absolute; left: 22px; top: 229px;
    font-family: "Open Sans", sans-serif; font-weight: 800;
    font-size: 36px; line-height: 44px; letter-spacing: 1px;
    color: var(--text-white);
  }
  .photo-side {
    position: absolute; right: 0; top: 0;
    width: 370px; height: 275px;
  }
</style>
</head>
<body>
  <main class="billboard">
    <h1 class="headline">
      <span class="headline-intro">Earn up to</span><span class="pay-badge">$90.000/year</span>
    </h1>

    <p class="company-name">Brisk Lane Freighters</p>
    <p class="website">www.brisklanefreighters.com</p>

    <div class="phone-band"></div>
    <p class="phone">503-217-6095</p>

    <svg class="photo-side" viewBox="0 0 370 275" aria-hidden="false">
      <defs>
        <linearGradient id="truckTone" x1="0" y1="0" x2="1" y2="1">
          <stop offset="0" stop-color="var(--truck-tone-light)"/>
          <stop offset="1" stop-color="var(--truck-tone-dark)"/>
        </linearGradient>
      </defs>
      <path d="M100 0 Q40 60 50 275 L370 275 L370 0 Z" fill="var(--accent-sky)"/>
      <path d="M125 0 Q60 70 72 275 L370 275 L370 0 Z" fill="var(--board-blue-deep)"/>
      <path d="M150 0 Q88 80 98 275 L370 275 L370 0 Z" fill="var(--text-white)"/>
      <path d="M172 0 Q110 90 118 275 L370 275 L370 0 Z" fill="var(--text-white)"/>
      <rect x="110" y="8" width="260" height="267" rx="14" fill="url(#truckTone)"
            role="img" aria-label="Photo of a pale green semi truck cab with chrome grille, seen from the front left"/>
    </svg>
  </main>
</body>
</html>
```